Brightleaf Dentistry - Flyer - Modern & Eye catching campaign flyer

Need front & back side full page flyer designs for both 1) Grand opening 2) On-going campaign.

Attached the new dental office logo.
Attached our other dental clinic flyer designs for content.

Target Market(s)

Cosmetic dentistry

Industry/Entity Type

Health Care

Requirements
Must have
• decent, modern and eye catching marketing flyers.
Nice to have
• - Nice space
• - Highlight phone number
• - Highlight special features like convenient hours, call or text, for all ages, digital facility, etc
Should not have
• - Don't want to fill the flyer with too much wordings
• - Too many colors

```html
<!DOCTYPE html>
<html lang="en">
<head>
<meta charset="utf-8">
<title>Brightleaf Dentistry Flyer</title>
<link href="https://fonts.googleapis.com/css2?family=Montserrat:wght@400;500;600&display=swap" rel="stylesheet">
<style>
:root{
  --cyan:#2fb2d8;
  --cyan-deep:#00aed6;
  --slate:#627a97;
  --slate-soft:#8092b0;
  --ice:#ddeef5;
  --ink:#4f5358;
  --name:#6a7fa0;
  --white:#ffffff;
}
*{margin:0;padding:0;box-sizing:border-box}
html,body{width:849px;height:1200px;overflow:hidden;background:var(--white)}
body{font-family:"Montserrat",Arial,sans-serif;color:var(--ink);position:relative}
.flyer{position:absolute;inset:0}
.contact-label{position:absolute;left:77px;top:106px;font-size:20px;font-weight:600;letter-spacing:1.2px;color:var(--slate)}
.contact-phone{position:absolute;left:76px;top:126px;font-size:33px;font-weight:600;letter-spacing:1px;color:var(--cyan)}
.divider{position:absolute;left:383px;top:102px;width:2px;height:62px;background:var(--slate)}
.brand{position:absolute;left:452px;top:116px;display:flex;align-items:center;gap:12px}
.brand-dot{width:26px;height:26px;border-radius:50%;background:var(--cyan)}
.brand-name{font-size:25px;font-weight:600;letter-spacing:.5px;color:var(--cyan)}
.hero-photo{position:absolute;left:21px;top:189px;width:806px;height:432px;
  background:linear-gradient(100deg,#e9ecec 0%,#d9d3cf 40%,#cfd8d6 60%,#e4e6e3 100%)}
.band{position:absolute;top:621px;height:100px;color:var(--white);font-size:24px;font-weight:600;letter-spacing:1.8px;line-height:29px;padding-top:25px}
.band-left{left:21px;width:403px;background:var(--cyan);padding-left:56px}
.band-right{left:424px;width:403px;background:var(--slate-soft);padding-left:41px}
.intro{position:absolute;left:77px;top:748px;width:320px;font-size:15.5px;line-height:19px;font-weight:400}
.doctor{position:absolute;left:77px;top:886px;font-size:24px;font-weight:400;letter-spacing:1.2px;color:var(--name)}
.features{position:absolute;left:424px;top:721px;width:403px;height:228px;background:var(--ice);list-style:none;padding:24px 30px 0 59px}
.features li{position:relative;font-size:14.6px;line-height:17px;margin-bottom:8px}
.features li::before{content:"";position:absolute;left:-15px;top:4px;width:10px;height:10px;border-radius:50%;background:var(--cyan-deep)}
.insurance{position:absolute;left:424px;top:949px;width:403px;height:100px;background:var(--cyan-deep);color:var(--white);
  text-align:center;font-size:26px;font-weight:600;letter-spacing:1.6px;line-height:31px;padding-top:18px}
.footer-band{position:absolute;left:21px;top:1049px;width:806px;height:95px;background:var(--slate)}
.map-frame{position:absolute;left:77px;top:957px;width:273px;height:187px;background:var(--slate)}
.map{position:absolute;left:14px;top:15px;width:245px;height:157px;background:linear-gradient(135deg,#e8e8e8,#dcdcdc 60%,#e6e3d8)}
.address{position:absolute;left:360px;top:1082px;display:flex;align-items:center;gap:12px;color:var(--white);font-size:18px;letter-spacing:1.6px}
</style>
</head>
<body>
<div class="flyer">
  <p class="contact-label">Call or Text Us Now:</p>
  <p class="contact-phone">610.555.0148</p>
  <div class="divider"></div>
  <div class="brand"><span class="brand-dot"></span><span class="brand-name">Brightleaf Dentistry</span></div>

  <div class="hero-photo" role="img" aria-label="Smiling dentist in a white coat with arms crossed in a bright dental treatment room"></div>

  <h2 class="band band-left">LOOKING FOR DENTIST<br>CLOSE TO HOME?</h2>
  <h2 class="band band-right">FAMILY &amp; COSMETIC<br>DENTISTRY</h2>

  <p class="intro">Come and See Us for Professional Services and Care. Our dentists and staff are experts in the field of advanced dentistry and will help you achieve your perfect smile.</p>
  <p class="doctor">Dr. Maya Holloway, D.D.S.</p>

  <ul class="features">
    <li>State-Of-The-Art equipment and paperless facility.</li>
    <li>Filled with entertainment devices for patient comfort.</li>
    <li>Same-day appointment for Dental Emergencies</li>
    <li>Helping community with routine free kids dental screening.</li>
  </ul>

  <div class="insurance">ALL INSURANCES<br>ACCEPTED</div>

  <div class="footer-band"></div>
  <div class="map-frame">
    <div class="map" role="img" aria-label="Street map showing the office location"></div>
  </div>
  <div class="address">
    <svg width="15" height="21" viewBox="0 0 15 21" aria-hidden="true">
      <path d="M7.5 0C3.4 0 0 3.3 0 7.4 0 12.5 7.5 21 7.5 21S15 12.5 15 7.4C15 3.3 11.6 0 7.5 0z" fill="#2fb2d8"/>
      <circle cx="7.5" cy="7.4" r="2.8" fill="#627a97"/>
    </svg>
    <span>412 Linden Pike, Maple Hill PA 19020</span>
  </div>
</div>
</body>
</html>
```